Need a design for coffee shop/bar

We need a simple site designed for a local coffee shop and bar. Small, locally owned place. Has live entertainment on occasion. Serves the business lunch and happy hour crowd as well and the baseball and basketball games fans. Located in downtown Cleveland. Looking for a simple site design with logo at top, horizontal main nav and slideshow and will need an interior page design as well (which will be used for general content like about, contact, menu, events, etc.) Would like it to be responsive. Current site is bvtellinos.com. Owner likes the color scheme, but open to changes.

*note - the owner roasts his own coffee and has a sister company for this called Marlow Bean Works (marlowbeanworks.com). We plan to use the exact same design for the coffee company's website, expect we'll swap out the logo at the top and use different photos. As part of the project we'd like a page designed that displays the various coffee products, but do not require this specific site be designed.

So, that makes three pages total. Home page (bvtellinos.com), interior and product page.

Target Market(s)

Young professionals, hipsters, sports fans, coffee and beer enthusiasts. Owner is into reggae and often has reggae bands.

Industry/Entity Type

Entertainment

Number of Pages Required

3 page

Requirements
Must have
• Slideshow, lot of images (some examples are on the current site, bvtellinos.com - client will be providing us with higher resolution images when we start development, so place holders are fine for the design). Responsive.

```html
<!DOCTYPE html>
<html lang="en">
<head>
<meta charset="utf-8">
<title>B.V.Tellino's — Menu</title>
<link rel="stylesheet" href="https://fonts.googleapis.com/css2?family=Arimo:wght@400;700&display=swap">
<style>
  :root {
    --hero-dark: #2a1a2e;
    --hero-mid: #4a2c45;
    --white: #ffffff;
    --rule: #e4e4e4;
    --rule-dark: #9a9a9a;
    --heading: #3a3a3a;
    --body: #5a5a5a;
    --footer-bg: #1c2328;
    --footer-text: #b8bcc0;
  }
  * { box-sizing: border-box; margin: 0; padding: 0; }
  html, body { width: 1200px; height: 2407px; overflow: hidden; background: var(--white); }
  body { position: relative; font-family: "Arimo", Arial, sans-serif; color: var(--body); }

  .hero {
    position: absolute; left: 0; top: 0; width: 1200px; height: 287px;
    background:
      radial-gradient(ellipse 300px 120px at 520px 200px, rgba(150,110,130,.55), transparent 70%),
      radial-gradient(ellipse 260px 140px at 240px 160px, rgba(110,70,90,.45), transparent 70%),
      linear-gradient(180deg, var(--hero-dark) 0%, var(--hero-mid) 60%, var(--hero-dark) 100%);
  }
  .site-header {
    position: absolute; left: 189px; top: 44px; width: 817px; height: 57px;
    border-bottom: 1px solid rgba(255,255,255,.35);
  }
  .brand {
    position: absolute; left: 0; top: 5px;
    font-weight: 700; font-size: 25px; letter-spacing: .5px; color: var(--white);
  }
  .main-nav { position: absolute; right: 0; top: 14px; display: flex; }
  .main-nav a { color: var(--white); text-decoration: none; font-size: 12px; margin-left: 34px; }
  .hero-tagline {
    position: absolute; left: 0; top: 134px; width: 1210px; text-align: center;
    color: var(--white); font-weight: 700; font-size: 32px; line-height: 41px;
  }

  .page-rule { position: absolute; left: 189px; top: 352px; width: 817px; border-top: 1px solid var(--rule); }
  .page-title {
    position: absolute; left: 0; top: 388px; width: 1192px; text-align: center;
    font-size: 28px; font-weight: 400; color: var(--heading); letter-spacing: .5px;
  }

  .menu-photo {
    position: absolute; left: 0; top: 480px; width: 418px; height: 1688px;
    background:
      radial-gradient(ellipse 260px 420px at 190px 250px, #1a1513 0%, transparent 80%),
      linear-gradient(180deg, #2e2218 0%, #3b2a1c 28%, #8a3a22 40%, #a0452a 60%, #7e3520 80%, #3a2418 100%);
  }

  .menu {
    position: absolute; left: 473px; top: 476px; width: 520px;
    font-size: 14.5px; line-height: 19.8px;
  }
  .menu p { margin-bottom: 19.8px; }
  .menu h3 { font-size: 14.5px; font-weight: 700; color: var(--body); text-transform: uppercase; }
  .menu-section { border-top: 1px solid var(--rule-dark); margin-top: -10px; padding-top: 9px; width: 532px; }
  .menu-section:first-child { border-top: none; margin-top: 0; padding-top: 0; }

  .site-footer {
    position: absolute; left: 0; top: 2341px; width: 1200px; height: 66px; background: var(--footer-bg);
  }
  .copyright { position: absolute; left: 189px; top: 30px; font-size: 11px; color: var(--footer-text); }
</style>
</head>
<body>
  <section class="hero" role="img" aria-label="Dim evening interior of the bar with set tables">
    <header class="site-header">
      <div class="brand">B.V.TELLINO'S</div>
      <nav class="main-nav">
        <a href="#">Home</a><a href="#">About</a><a href="#">Menu</a><a href="#">Activities</a><a href="#">Contact</a>
      </nav>
    </header>
    <h1 class="hero-tagline">From early in the morning<br>till late in the evening</h1>
  </section>

  <div class="page-rule"></div>
  <h2 class="page-title">MENU</h2>

  <div class="menu-photo" role="img" aria-label="Pint of stout beside a pepperoni pizza"></div>

  <main class="menu">
    <div class="menu-section">
      <h3>Daily Specials</h3>
      <p>Monday - Turkey Club w side $6.75<br>Tuesday - Tuna Melt w side $6.50<br>Wednesday - The Jake w side $6.50<br>Thursday - Corned Beef or Turkey Reubens w side $7<br>Friday - Grilled Cheese and Tomato Soup $6</p>
      <p>Daily soup with the option of a half traditional sandwich.</p>
      <p>We feature premium Hearthstone Deli.</p>
    </div>
    <div class="menu-section">
      <h3>Oven Baked Ciabatta Specialties</h3>
      <p></p>
      <p>CAXTON - $8.25<br>Seasoned chicken breast, red pepper, pesto, provolone, red onion, lettuce and tomato.</p>
      <p>ITALIAN SANGUINI - $8<br>Capiacola ham layered with salami, pepperoni, provolone,green pepper, red onion, lettuce and tomato.</p>
      <p>DOWNTOWNER - $7.50<br>Delux ham, salami, swiss cheese topped with chopped pickles and spicy dijon mustard.</p>
      <p>HOMETEAMER - $8<br>Seasoned roast beef, turkey and provolone topped with cole slaw, lettuce and tomato.</p>
      <p>THE JAKE - $7.50<br>Seasoned roast beef, peppercorn BBQ sauce, red onion and cheddar cheese.</p>
      <p>All Sandwiches feature Hearthstone Deli and Lakeshore Breads.</p>
    </div>
    <div class="menu-section">
      <h3>Veggie Bakes</h3>
      <p></p>
      <p>CLE-VEG - $7.25<br>Portabella mushroom, red pepper, red onion, cheddar cheese tzatziki sauce, lettuce and tomato.</p>
      <p>BAKED ARTICHOKE - $7.25<br>Artichoke hearts, sun-dried tomato, portabella mushroom, garlic sauce,<br>provolone cheese and rosmary.</p>
      <p>FLAT BREAD PIZZAS 12"</p>
      <p>Plain - $9.25<br>Pepperoni - $10.75<br>Bar-b-que- $12.25<br>Veggie - $12</p>
    </div>
    <div class="menu-section">
      <h3>Veggie</h3>
      <p></p>
      <p>MARKET VEGGIE - $6.95<br>Pita, spread of hummus, sprouts, kalamata olives, cucumbers, red onion,<br>lettuce and tomato.</p>
      <p>HUMMUS PLATTER - $6.75<br>Hummus bowl seasoned with paprika and kalamata olives, accompanied by pita triangles, sliced cucumbers and baby carrots.</p>
      <p>RED PEPPER HUMMUS - $6.95<br>Red pepper hummus, feta, baby spinach, cucumber and tomato in a whole<br>grain wrap.</p>
      <p>SALADS<br>Chef - $7.95<br>Chicken - $7.50<br>Garden - $5.75</p>
    </div>
    <div class="menu-section">
      <h3>Traditionals</h3>
      <p></p>
      <p>Turkey Club - $7.25<br>Hearthroast Turkey - $6.5<br>Delux Ham - $6<br>Top Corned Beef - $6.75<br>Seasoned Roast Beef - $6.75<br>*Corned Beef Rueben - $7.95<br>*Turkey Rueben - $7.95<br>Chicken Salad - $6.95<br>*Tuna Melt - $7.5<br>Tuna Salad - $6.95<br>Grilled Cheese - $5<br>BLT - $6<br>Egg Salad - $5.5<br>PBJ - $4.75</p>
      <p>*=HOT</p>
    </div>
  </main>

  <footer class="site-footer">
    <p class="copyright">© Copyright ©2015 BV Tellino's, All Rights Reserved.</p>
  </footer>
</body>
</html>
```